Feature film 1 sheet for action/thriller

I'm a writer/producer attending the Northgate Screen Exchange (NSE) in LA next month & I need a "one sheet" for the projects on my slate, starting with an action/thriller, Copper Ledger - which is also being developed as a graphic novel.
The logline is: After being forced to infiltrate a white supremacist terror cell by a renegade cop, an ex-convict tries to save the son he never knew from the extremists’ malign influence.
The full synopsis is attached as a Word file.
The story is set mostly in the arid desert of Southern California near the border with Mexico. Its themes involve choosing between keeping your head down vs. protecting family/loved ones; about being caught between law enforcement and outlaws (in the form of a white supremacist gang); about identity, race, loyalty & illegal immigration.
Because it hasn't been made there are no images from the film. I've uploaded an earlier version of the cover page of the graphic novel (not the final one), as well as a couple of sketches which are works in progress for a new cover. These are NOT images to actually use in the final design, but rather illustrations of the characters and ideas/themes/locations/imagery contained in the script. (Such as the swastika.)
The final "poster" will be A4 or letter-sized and double-sided.
The front should be similar to a movie poster. It should contain the text:
"Lantern Hollow Productions presents
COPPER LEDGER
An action/thriller feature film and graphic novel"
Along with the tag line: "Caught between the law and the lawless..."
The back should have the logline, synopsis and contact details. (See Word files attached). The company's logo is also attached as a file and should be included in the corner on the back.
I was going to mention (or attach) some examples of movie posters I like in this genre, but I decided I'd rather let designers come at it without those preconceptions. Also, clearly I don't have the advantage of any shots of the stars of the film or any stills from the film (as it hasn't been made), and I figured that will most likely influence the type of design choices that can be made.
A few final thoughts that might help inspiration: Given the desert location, I wondered about the use of red/orange/yellow (perhaps with bold black text?). Also, there's a climactic scene that takes place in Salton Sea in CA (see attached image or Google it). I will be pitching this to producers, distributors and sales agents, but the ultimate target audience for the film would skew male and likely be predominantly 16-39.
Movie
- Possibly all caps Stencil font for the title

```html
<!DOCTYPE html>
<html lang="en">
<head>
<meta charset="utf-8">
<title>Copper Ledger — One Sheet (Back)</title>
<link rel="stylesheet" href="https://fonts.googleapis.com/css2?family=Barlow:wght@300;400;600&display=swap">
<style>
  :root {
    --ink: #050505;
    --ember: #c4551a;
    --ember-deep: #3a1608;
    --headline: #f4f2ef;
    --body: #d9d6d2;
    --contact: #e8e6e3;
    --mark: #c9632a;
  }
  * { margin: 0; padding: 0; box-sizing: border-box; }
  html, body { width: 848px; height: 1200px; overflow: hidden; background: var(--ink); }
  .sheet {
    position: relative;
    width: 848px;
    height: 1200px;
    overflow: hidden;
    font-family: "Barlow", "Helvetica Neue", Arial, sans-serif;
    color: var(--body);
  }
  .sheet__backdrop { position: absolute; inset: 0; width: 100%; height: 100%; }
  .logline {
    position: absolute;
    left: 117px;
    top: 46px;
    width: 684px;
    font-weight: 400;
    font-size: 27.4px;
    line-height: 38px;
    color: var(--headline);
    letter-spacing: 0.1px;
  }
  .synopsis {
    position: absolute;
    left: 114px;
    top: 312px;
    width: 684px;
    font-size: 11.6px;
    line-height: 14.7px;
    text-align: justify;
    font-weight: 400;
  }
  .synopsis p { margin-bottom: 14.5px; }
  .synopsis p.tight { margin-bottom: 0; }
  .contact {
    position: absolute;
    left: 0;
    top: 1050px;
    width: 848px;
    height: 100px;
    color: var(--contact);
  }
  .contact__mark {
    position: absolute;
    left: 40px;
    top: 12px;
    width: 62px;
    height: 62px;
    border-radius: 50%;
    background: var(--mark);
  }
  .contact__name {
    position: absolute;
    left: 116px;
    top: 10px;
    font-size: 23px;
    font-weight: 400;
    line-height: 28px;
  }
  .contact__company {
    position: absolute;
    left: 116px;
    top: 43px;
    font-size: 14.5px;
    font-weight: 400;
    letter-spacing: 0.4px;
    text-transform: uppercase;
  }
  .contact__address, .contact__lines {
    position: absolute;
    top: 16px;
    font-size: 11.6px;
    line-height: 14px;
  }
  .contact__address { left: 360px; }
  .contact__lines { left: 588px; }
</style>
</head>
<body>
<main class="sheet">
  <svg class="sheet__backdrop" viewBox="0 0 848 1200" preserveAspectRatio="none" role="img" aria-label="Orange sparks flying across a black background">
    <defs>
      <radialGradient id="ember-glow-top" cx="0.75" cy="0.15" r="0.6">
        <stop offset="0" stop-color="#4a1d0a" stop-opacity="0.85"/>
        <stop offset="1" stop-color="#050505" stop-opacity="0"/>
      </radialGradient>
      <radialGradient id="ember-glow-low" cx="0.8" cy="0.7" r="0.55">
        <stop offset="0" stop-color="#3a1608" stop-opacity="0.7"/>
        <stop offset="1" stop-color="#050505" stop-opacity="0"/>
      </radialGradient>
    </defs>
    <rect width="848" height="1200" fill="#060606"/>
    <rect width="848" height="1200" fill="url(#ember-glow-top)"/>
    <rect width="848" height="1200" fill="url(#ember-glow-low)"/>
  </svg>

  <h1 class="logline">After being forced to infiltrate a white supremacist terror cell by a renegade cop, an ex-convict tries to save the son he never knew from the extremists’ malign influence.</h1>

  <section class="synopsis">
    <p>Joe Tanner (30’s) is haunted by his past. An ex Border Patrol officer, he was tangentially involved in the killing of illegal aliens by vigilantes a decade earlier. Now he’s being released from jail, after giving secret testimony that put the vigilantes’ leader (Duke) in prison for life.</p>
    <p>He enters witness protection under the supervision of U.S. Marshal Neena Rodriegez. She has little time for him, believing (incorrectly) that he’s an unrepentant racist. Joe keeps a low profile, but he’s being watched. The stalker turns out to be a cop – Andrews. He wants Joe to infiltrate the vigilante gang – now led by Duke’s brother, Robbie – and convince his old flame, Belle, to also turn state’s evidence. Joe is reluctant until Andrews reveals Joe has a son, Nick (10), who’ll soon be initiated into the gang. Joe agrees to go undercover.</p>
    <p>He joins the gang and his initiation rites culminate in a “hit” that – despite efforts by Andrews – leads to the target’s death. However, it also leads to Robbie confiding in Joe about a planned bank heist where Joe’s expert electronics skills will be put to use. Andrews plans to catch the gang in the act, but the location is changed at the last minute and Andrews’ men are at the wrong bank. Belle is wounded (callously shot by Andrews) and Joe – keen to look out for Belle and Nick – “escapes” with the gang.</p>
    <p class="tight">A furious Rodriegez confronts Andrews and he unceremoniously murders her. He then publicly pins the murder on Joe, leaving him utterly isolated: in danger from both the criminals and the authorities.</p>
    <p>Joe wants to take Nick and the wounded Belle and get away from the gang. However Robbie insists he help them free Duke from jail. Joe gives them the information they need to over-ride the security system but Robbie reneges on the deal, executing Belle and telling Nick it was Joe who killed her. But Nick can’t bring himself to kill Joe as Robbie instructs and Joe escapes. He hooks up with Nick – who’s also fled, traumatized and alone – and convinces Nick of his innocence.</p>
    <p>Aided by his former cellmate, Joe confronts Andrews. Meanwhile, Nick discovers it was Andrews who shot Belle during the bank heist. Joe has just realized Andrews is collaborating with Duke when Nick shoots Andrews to avenge his mother. Robbie and the gang free Duke from Belle’s funeral (the motivation for her murder). They then embark on their master plan: using Duke’s expertise to launch a poison gas attack on a Mexican border town.</p>
    <p>In a final showdown, Joe does enough to thwart the gang’s plans until the Feds arrive, and a critically wounded Robbie inadvertently shoots his brother, Duke.</p>
    <p>Distrustful of authority but determined to be the father that Nick deserves, Joe “disappears” with Nick to a place where they can start their lives over again, together.</p>
  </section>

  <footer class="contact">
    <span class="contact__mark" aria-hidden="true"></span>
    <div class="contact__name">Rowan Keats</div>
    <div class="contact__company">Lantern Hollow Productions</div>
    <address class="contact__address" style="font-style: normal;">P O Box 48-2210<br>Kestrel Bay 0815<br>NEW ZEALAND</address>
    <div class="contact__lines">+00-21-555-0142<br>info@lanternhollow-productions.com<br>www.lanternhollowproductions.com</div>
  </footer>
</main>
</body>
</html>
```